Create business card template

I need to create a simple, elegant and minimalistic business card template that I can use for also future people, so not only just for me.

I want ideas for it and to be quite printer friendly! I already have the company logo in vectorial format ant that has to be used in the business card format. I envision a black minimalistic design with a QR code. I accept all kind of ideas, metal or finishes in different looking materials, but I want to avoid wood or something that resembles old stuff. I need something modern, fresh and something that's in tune with out digital world since the QR code idea.

I need the end result in many known file formats and mandatory vectorial !! The size should be the same with a credit card, so no weird looking aspects.

THE IDEA HAS TO BE ORIGINAL! So please don't rush into business card software templates and in 2 minutes propose!

I'm willing to negotiate on the price if the idea is done from scratch and is completely original and much thought has been put into the work. I also uploaded a logo of the site to give you an idea!

```html
<!DOCTYPE html>
<html lang="en">
<head>
<meta charset="UTF-8">
<title>Vantor Studio — Business Card</title>
<link rel="stylesheet" href="https://fonts.googleapis.com/css2?family=Montserrat:wght@300;400;500;600;700&display=swap">
<style>
  :root {
    --page-bg: #e7e6e3;
    --card-stock: #6d6d70;
    --card-stock-dark: #616164;
    --ink: #f4f4f4;
    --ink-soft: #d9d9db;
  }
  * { margin: 0; padding: 0; box-sizing: border-box; }
  html, body { width: 1200px; height: 900px; overflow: hidden; }
  body {
    background: var(--page-bg);
    font-family: "Montserrat", sans-serif;
    color: var(--ink);
    display: flex;
    align-items: center;
    justify-content: center;
    gap: 60px;
  }
  .card {
    position: relative;
    width: 520px;
    height: 328px;
    border-radius: 30px;
    background: radial-gradient(circle at 40% 35%, var(--card-stock), var(--card-stock-dark));
    box-shadow: 0 10px 28px rgba(0,0,0,0.18);
    overflow: hidden;
  }
  .brand-name { white-space: nowrap; text-transform: uppercase; line-height: 1; }
  .brand-dot { border-radius: 50%; flex: none; }

  /* Front */
  .front .lockup {
    position: absolute;
    left: 0; right: 0;
    top: 100px;
    display: flex;
    justify-content: center;
  }
  .lockup-inner {
    display: inline-flex;
    flex-direction: column;
    align-items: flex-end;
    gap: 14px;
  }
  .front .brand {
    display: flex;
    align-items: center;
    gap: 16px;
  }
  .front .brand-dot { width: 44px; height: 44px; background: var(--ink); }
  .front .brand-name {
    font-weight: 600;
    font-size: 32px;
    letter-spacing: 2px;
    color: var(--ink);
  }
  .front .brand-rule {
    width: 240px;
    height: 1.5px;
    background: var(--ink);
  }
  .front .website {
    position: absolute;
    left: 0; right: 0;
    bottom: 46px;
    text-align: center;
    font-size: 15px;
    font-weight: 500;
    letter-spacing: 5px;
    text-transform: uppercase;
    color: var(--ink);
  }

  /* Back */
  .back .contacts {
    position: absolute;
    left: 34px;
    top: 96px;
    list-style: none;
    display: flex;
    flex-direction: column;
    gap: 12px;
  }
  .contact-item {
    display: flex;
    align-items: center;
    gap: 10px;
    font-size: 11px;
    font-weight: 400;
    color: var(--ink-soft);
    white-space: nowrap;
  }
  .contact-icon { width: 12px; height: 12px; flex: none; }
  .back .center-mark {
    position: absolute;
    left: 290px;
    top: 118px;
    display: flex;
    align-items: center;
    gap: 10px;
  }
  .center-mark .brand-dot { width: 22px; height: 22px; background: var(--ink-soft); }
  .center-mark .brand-name { font-size: 16px; font-weight: 600; letter-spacing: 1.5px; color: var(--ink-soft); }
  .back .holder {
    position: absolute;
    right: 40px;
    top: 208px;
    text-align: right;
    padding-right: 14px;
    border-right: 2px solid var(--ink);
  }
  .holder-name { font-size: 17px; font-weight: 700; color: var(--ink); }
  .holder-role { font-size: 11px; font-weight: 400; color: var(--ink-soft); margin-top: 2px; }
</style>
</head>
<body>

  <section class="card front">
    <div class="lockup">
      <div class="lockup-inner">
        <div class="brand">
          <span class="brand-dot"></span>
          <span class="brand-name">Vantor Studio</span>
        </div>
        <div class="brand-rule"></div>
      </div>
    </div>
    <p class="website">www.vantorstudio.co.uk</p>
  </section>

  <section class="card back">
    <ul class="contacts">
      <li class="contact-item">
        <svg class="contact-icon" viewBox="0 0 24 24"><path fill="#f4f4f4" d="M6.6 10.8a15 15 0 0 0 6.6 6.6l2.2-2.2c.3-.3.7-.4 1-.2 1.1.4 2.3.6 3.6.6.6 0 1 .4 1 1V20c0 .6-.4 1-1 1A17 17 0 0 1 3 4c0-.6.4-1 1-1h3.5c.6 0 1 .4 1 1 0 1.3.2 2.5.6 3.6.1.3 0 .7-.2 1z"/></svg>
        +012 555 0142
      </li>
      <li class="contact-item">
        <svg class="contact-icon" viewBox="0 0 24 24"><circle cx="12" cy="12" r="11" fill="#f4f4f4"/><path d="M6 9l6 4 6-4" stroke="#6d6d70" stroke-width="2" fill="none"/></svg>
        hello@vantorstudio.com
      </li>
      <li class="contact-item">
        <svg class="contact-icon" viewBox="0 0 24 24"><circle cx="12" cy="12" r="10" fill="none" stroke="#f4f4f4" stroke-width="2"/><path d="M2 12h20M12 2c3 3 3 17 0 20M12 2c-3 3-3 17 0 20" stroke="#f4f4f4" stroke-width="1.5" fill="none"/></svg>
        www.vantorstudio.com
      </li>
      <li class="contact-item">
        <svg class="contact-icon" viewBox="0 0 24 24"><path fill="#f4f4f4" d="M12 2a7 7 0 0 0-7 7c0 5 7 13 7 13s7-8 7-13a7 7 0 0 0-7-7zm0 9.5A2.5 2.5 0 1 1 12 6.5a2.5 2.5 0 0 1 0 5z"/></svg>
        18 Linden Row, Halford, Texas 75010
      </li>
    </ul>

    <div class="center-mark">
      <span class="brand-dot"></span>
      <span class="brand-name">Vantor Studio</span>
    </div>

    <div class="holder">
      <p class="holder-name">Mara Quill</p>
      <p class="holder-role">Founder &amp; CEO</p>
    </div>
  </section>

</body>
</html>
```